Elderwell Solutions company needs a homepage design

We need a homepage designed for a new company based in Des Moines, IA called Go Elderwell Solutions. They sell Elderwell Supplement plans to seniors. The design should communicate trust, security, be vibrant and easy to read with larger font and clear messages. The goal for visitors is to ultimately get a free quote and purchase a plan after a call from a licensed agent.

Industry/Entity Type

It Company

```html
<!DOCTYPE html>
<html lang="en">
<head>
<meta charset="utf-8">
<title>Go Elderwell Solutions – Home</title>
<link href="https://fonts.googleapis.com/css2?family=Open+Sans:wght@400;600;700&family=Raleway:wght@400;600;700;800&display=swap" rel="stylesheet">
<style>
:root{
  --blue:#1d9bd7;
  --blue-light:#29ade2;
  --blue-dark:#1786c2;
  --ink:#3c3c3c;
  --muted:#7d7d7d;
  --line:#e3e6e9;
  --panel:#f4f6f8;
  --dark:#2e3033;
  --white:#ffffff;
}
*{box-sizing:border-box;margin:0;padding:0}
html,body{width:1200px;height:3212px;overflow:hidden}
body{position:relative;background:var(--white);font-family:"Open Sans",Arial,sans-serif;color:var(--ink);font-size:13px}
.abs{position:absolute}
h2,h3,h4{font-family:"Raleway",Arial,sans-serif}

/* top bar + nav */
.topbar{left:0;top:0;width:1200px;height:32px;background:var(--blue);color:var(--white);font-size:12px;display:flex;align-items:center;padding:0 70px;gap:26px}
.topbar span{display:flex;align-items:center;gap:6px}
.topbar .social{margin-left:auto;display:flex;gap:8px}
.topbar .social i{width:14px;height:14px;border-radius:50%;background:rgba(255,255,255,.7);display:block}
.nav{left:0;top:32px;width:1200px;height:128px;display:flex;align-items:center;padding:0 70px}
.brand{display:flex;align-items:center;gap:12px;font-family:"Raleway",sans-serif;font-weight:700;font-size:38px;color:var(--blue)}
.brand i{width:42px;height:42px;background:var(--blue);display:block;border-radius:4px}
.menu{margin-left:auto;display:flex}
.menu a{font-size:11px;font-weight:600;color:var(--ink);text-decoration:none;padding:10px 18px;letter-spacing:.5px}
.menu a.on{background:var(--blue);color:var(--white)}

/* hero */
.hero{left:0;top:160px;width:1200px;height:500px;background:linear-gradient(100deg,#cfe4ee 0%,#e9f2f6 35%,#dbe9ef 70%,#c3dbe6 100%)}
.hero-bubble{left:720px;top:230px;width:260px;height:260px;border-radius:50%;background:rgba(41,173,226,.82);color:var(--white);display:flex;align-items:center;justify-content:center;text-align:center;font-family:"Raleway",sans-serif;font-size:21px;font-weight:600;line-height:1.35;padding:36px}
.hero-dot{left:950px;top:440px;width:80px;height:80px;border-radius:50%;background:var(--blue);color:var(--white);font-size:11px;font-weight:600;display:flex;align-items:center;justify-content:center;text-align:center;line-height:1.3}

/* features */
.feature{top:700px;width:240px;height:300px;background:var(--panel);text-align:center;padding:46px 20px 0}
.feature svg{display:block;margin:0 auto 18px}
.feature h3{font-size:20px;font-weight:600;color:var(--ink);margin-bottom:14px}
.feature p{font-size:12px;color:var(--muted);line-height:1.55}
.btn{display:inline-block;background:var(--blue);color:var(--white);font-size:11px;font-weight:600;padding:8px 20px;letter-spacing:.4px}
.feature .btn{position:absolute;left:50%;transform:translateX(-50%);bottom:-16px;white-space:nowrap}

/* about / plans band */
.about{left:0;top:1240px;width:600px;height:400px;background:var(--blue-light)}
.services{left:600px;top:1240px;width:600px;height:400px;background:var(--blue-dark)}
.about-text{left:80px;top:1275px;width:265px;color:var(--white)}
.eyebrow{font-size:10px;letter-spacing:1px;text-transform:uppercase;opacity:.85}
.about-text h2{font-size:21px;font-weight:700;margin:4px 0 12px;white-space:nowrap}
.about-text .lead{font-size:15px;font-weight:600;line-height:1.4;margin-bottom:14px}
.about-text p{font-size:12px;line-height:1.55;opacity:.92}
.ghost{display:inline-block;border:1px solid var(--white);color:var(--white);font-size:12px;padding:8px 18px;margin-top:16px}
.doctor{left:350px;top:1270px;width:300px;height:370px;background:linear-gradient(180deg,#8fd2ef,#5ab6df);border-radius:150px 150px 0 0}
.services-text{left:660px;top:1275px;width:480px;color:var(--white)}
.services-text h2{font-size:26px;font-weight:700;margin:4px 0 12px}
.services-text p{font-size:12px;line-height:1.55;opacity:.92;width:300px;margin-bottom:22px}
.svc-list{display:grid;grid-template-columns:1fr 1fr;gap:14px 20px;list-style:none}
.svc-list li{font-size:13px;font-weight:700;display:flex;align-items:center;gap:10px;letter-spacing:.3px;white-space:nowrap}
.svc-list li::before{content:"";width:7px;height:7px;background:var(--white);flex:none}
.hex{left:568px;top:1590px}

/* senior coverage */
.neuro{left:80px;top:1710px;width:250px;border-left:3px solid var(--blue);padding-left:22px}
.neuro small{display:block;font-family:"Raleway",sans-serif;font-size:26px;color:var(--blue);font-weight:400}
.neuro h3{font-size:26px;font-weight:700;color:var(--blue);margin-bottom:16px;line-height:1.15}
.neuro p{font-size:12px;color:var(--muted);line-height:1.6}
.neuro a{display:block;margin-top:14px;font-size:12px;color:var(--blue);text-decoration:none}
.benefits{left:370px;top:1710px;width:380px}
.benefits h4{font-size:14px;font-weight:700;color:var(--ink);margin-bottom:12px}
.benefits ul{list-style:none}
.benefits li{display:flex;align-items:center;gap:10px;font-size:12.5px;color:var(--muted);padding:6px 0;border-bottom:1px solid var(--line)}
.scan{left:820px;top:1720px;width:300px;height:180px;background:linear-gradient(120deg,#dfe8ee,#b9cad6)}

/* free quote band */
.appt{left:60px;top:2070px;width:1070px;height:110px;background:var(--blue-light)}
.appt-photo{left:90px;top:2064px;width:150px;height:116px;background:linear-gradient(180deg,#cfeaf6,#84c9e8)}
.appt-text{left:270px;top:2100px;color:var(--white)}
.appt-text h3{font-size:18px;font-weight:700}
.appt-text p{font-size:12px;opacity:.92;margin-top:4px}
.appt-btn{left:540px;top:2108px;border:1px solid var(--white);color:var(--white);font-size:11px;font-weight:600;padding:10px 24px}
.call{left:820px;top:2070px;width:310px;height:110px;background:var(--blue-dark);color:var(--white);display:flex;align-items:center;gap:16px;padding:0 26px}
.call small{display:block;font-size:11px;opacity:.9}
.call strong{font-size:29px;font-family:"Raleway",sans-serif;font-weight:700;white-space:nowrap}

/* testimonials */
.testi{left:0;top:2230px;width:1200px;text-align:center}
.testi h2{font-size:40px;font-weight:700;color:var(--blue)}
.testi p{width:820px;margin:14px auto 0;font-size:12.5px;color:var(--muted);line-height:1.6}
.avatar{width:72px;height:72px;border-radius:50%;background:linear-gradient(#d8e4ea,#b6c8d2);margin:26px auto 10px}
.testi .name{font-size:12px;font-weight:700;color:var(--ink)}
.testi .role{font-size:11px;color:var(--muted)}
.dots{display:flex;gap:6px;justify-content:center;margin-top:14px}
.dots i{width:8px;height:8px;border-radius:50%;background:var(--line)}
.dots i.on{background:var(--blue)}

/* contact */
.contact{left:0;top:2560px;width:1200px;height:620px;background:var(--dark)}
.contact-title{left:0;top:2620px;width:1200px;text-align:center;color:var(--white);font-family:"Raleway",sans-serif;font-size:30px;font-weight:700}
.form{left:120px;top:2740px;width:420px;height:360px;background:var(--white);padding:26px 28px}
.form h4{font-size:17px;font-weight:600;margin-bottom:18px}
.field{height:32px;border:1px solid var(--line);background:var(--panel);font-size:12px;color:var(--muted);padding:8px 10px;margin-bottom:12px}
.field.big{height:100px}
.form .btn{float:right}
.info{left:600px;top:2740px;width:520px;color:var(--white)}
.info h3{font-size:24px;font-weight:600;margin-bottom:24px}
.offices{display:grid;grid-template-columns:1fr 1fr;gap:26px 30px}
.office h4{font-size:15px;font-weight:700;margin-bottom:10px}
.office p{display:flex;gap:10px;font-size:12px;line-height:1.5;color:#cfd3d6;margin-bottom:8px}
.book{left:1000px;top:3030px;background:var(--blue);color:var(--white);font-size:12px;font-weight:700;padding:14px 26px}
.footer{left:0;top:3180px;width:1200px;height:32px;background:var(--blue);color:var(--white);font-size:11px;display:flex;align-items:center;justify-content:center}
</style>
</head>
<body>

<div class="abs topbar">
  <span><svg width="12" height="12" viewBox="0 0 24 24" fill="#fff"><path d="M6.6 10.8a15 15 0 006.6 6.6l2.2-2.2a1 1 0 011-.25 11.4 11.4 0 003.6.57 1 1 0 011 1V20a1 1 0 01-1 1A17 17 0 013 4a1 1 0 011-1h3.5a1 1 0 011 1c0 1.25.2 2.45.57 3.6a1 1 0 01-.25 1z"/></svg>(515) 555-0142</span>
  <span><svg width="13" height="11" viewBox="0 0 24 18" fill="#fff"><path d="M0 0h24v18H0zM2 2l10 8 10-8"/></svg>care@elderwell.example</span>
  <div class="social"><i></i><i></i><i></i><i></i></div>
</div>

<header class="abs nav">
  <div class="brand"><i></i>Elderwell</div>
  <nav class="menu">
    <a class="on">HOME</a><a>ABOUT US</a><a>WHY JOIN US</a><a>PLANS</a><a>FAQ</a><a>CONTACT US</a>
  </nav>
</header>

<div class="abs hero" role="img" aria-label="Photo of a friendly care advisor in a bright clinic corridor"></div>
<div class="abs hero-bubble">Go Elderwell – Supplement Plans for Iowa Seniors</div>
<div class="abs hero-dot">Free<br>Quote</div>

<div class="abs feature" style="left:68px">
  <svg width="44" height="40" viewBox="0 0 44 40" fill="none" stroke="#1d9bd7" stroke-width="2.5"><path d="M22 37S3 25 3 13a9.5 9.5 0 0119-2 9.5 9.5 0 0119 2c0 12-19 24-19 24z"/><path d="M9 19h8l3-5 4 9 3-4h8"/></svg>
  <h3>Health Coverage</h3>
  <p>Elderwell Supplement plans help pay the costs basic cover leaves behind, so seniors keep more of their savings.</p>
  <span class="btn">Read More</span>
</div>
<div class="abs feature" style="left:340px">
  <svg width="40" height="40" viewBox="0 0 40 40" fill="#1d9bd7"><rect x="2" y="10" width="36" height="26" rx="3"/><rect x="14" y="4" width="12" height="8" fill="none" stroke="#1d9bd7" stroke-width="2.5"/><path d="M17 16h6v5h5v6h-5v5h-6v-5h-5v-6h5z" fill="#fff"/></svg>
  <h3>Compare Plans</h3>
  <p>We compare top supplement plans side by side and explain each one in plain words, with no pressure to buy.</p>
  <span class="btn">Read More</span>
</div>
<div class="abs feature" style="left:608px">
  <svg width="40" height="40" viewBox="0 0 40 40" fill="#1d9bd7"><path d="M20 2L3 8v12c0 9 7 16 17 18 10-2 17-9 17-18V8z"/><path d="M13 20l5 5 9-10" fill="none" stroke="#fff" stroke-width="3"/></svg>
  <h3>Licensed Agents</h3>
  <p>A licensed agent from Des Moines calls you back, answers every question and helps you enroll with confidence.</p>
  <span class="btn">Read More</span>
</div>
<div class="abs feature" style="left:880px">
  <svg width="44" height="40" viewBox="0 0 44 40" fill="#1d9bd7"><path d="M12 34a10 10 0 0120 0z"/><rect x="6" y="34" width="32" height="5"/><path d="M22 4v8M8 10l5 5M36 10l-5 5M2 24h7M35 24h7" stroke="#1d9bd7" stroke-width="2.5"/></svg>
  <h3>Free Quote</h3>
  <p>Get a free quote in minutes. Tell us your zip code and age and we find the best rate for your budget.</p>
  <span class="btn">Read More</span>
</div>

<div class="abs about"></div>
<div class="abs services"></div>
<div class="abs about-text">
  <div class="eyebrow">Our Story</div>
  <h2>ABOUT GO ELDERWELL</h2>
  <div class="lead">Trusted supplement plans for seniors, backed by people who care.</div>
  <p>Go Elderwell Solutions was founded in Des Moines, Iowa to make supplement plans simple. We listen first, compare honestly and stay with you long after you enroll, so your coverage keeps pace with your life.</p>
  <span class="ghost">Know More</span>
</div>
<div class="abs doctor" role="img" aria-label="Photo of a smiling licensed agent wearing a headset"></div>
<div class="abs services-text">
  <div class="eyebrow">Plans You Can Rely On</div>
  <h2>OUR PLANS</h2>
  <p>Every plan we offer is clear about what it covers and what it costs. Pick the one that fits your health, your doctors and your budget.</p>
  <ul class="svc-list">
    <li>SUPPLEMENT PLAN G</li><li>SUPPLEMENT PLAN N</li>
    <li>HIGH DEDUCTIBLE PLAN G</li><li>DENTAL &amp; VISION</li>
    <li>PRESCRIPTION PLANS</li><li>HEARING COVERAGE</li>
    <li>HOSPITAL INDEMNITY</li><li>PLAN REVIEWS</li>
    <li>NEW TO 65 HELP</li><li>ANNUAL RATE CHECKS</li>
  </ul>
</div>
<svg class="abs hex" width="64" height="72" viewBox="0 0 64 72"><path d="M32 2l29 17v34L32 70 3 53V19z" fill="#fff"/><path d="M32 24l12 10-12 12-12-12z" fill="none" stroke="#1d9bd7" stroke-width="3"/></svg>

<div class="abs neuro">
  <small>BEST IN IOWA</small>
  <h3>SENIOR COVERAGE</h3>
  <p>Turning 65 or changing plans? Our team makes the choice easy, with clear answers for you and your family.</p>
  <a>Know more ›</a>
</div>
<div class="abs benefits">
  <h4>QUICK LOOK AT BENEFITS</h4>
  <ul>
    <li><svg width="14" height="14" viewBox="0 0 14 14"><path d="M2 7l3 3 7-7" stroke="#1d9bd7" stroke-width="2" fill="none"/></svg>Licensed, local agents</li>
    <li><svg width="14" height="14" viewBox="0 0 14 14"><path d="M2 7l3 3 7-7" stroke="#1d9bd7" stroke-width="2" fill="none"/></svg>Keep the doctors you already trust</li>
    <li><svg width="14" height="14" viewBox="0 0 14 14"><path d="M2 7l3 3 7-7" stroke="#1d9bd7" stroke-width="2" fill="none"/></svg>Free quotes with no obligation</li>
    <li><svg width="14" height="14" viewBox="0 0 14 14"><path d="M2 7l3 3 7-7" stroke="#1d9bd7" stroke-width="2" fill="none"/></svg>Save money on out-of-pocket costs</li>
    <li><svg width="14" height="14" viewBox="0 0 14 14"><path d="M2 7l3 3 7-7" stroke="#1d9bd7" stroke-width="2" fill="none"/></svg>Easy enrollment by phone</li>
  </ul>
</div>
<div class="abs scan" role="img" aria-label="Photo of a senior couple reviewing plans with an agent"></div>

<div class="abs appt"></div>
<div class="abs appt-photo" role="img" aria-label="Photo of a licensed agent with arms crossed"></div>
<div class="abs appt-text"><h3>GET YOUR FREE QUOTE</h3><p>It's easy and free, request it now!</p></div>
<div class="abs appt-btn">GET QUOTE</div>
<div class="abs call">
  <svg width="32" height="32" viewBox="0 0 24 24" fill="#fff"><path d="M6.6 10.8a15 15 0 006.6 6.6l2.2-2.2a1 1 0 011-.25 11.4 11.4 0 003.6.57 1 1 0 011 1V20a1 1 0 01-1 1A17 17 0 013 4a1 1 0 011-1h3.5a1 1 0 011 1c0 1.25.2 2.45.57 3.6a1 1 0 01-.25 1z"/></svg>
  <div><small>CALL A LICENSED AGENT</small><strong>515 555 0190</strong></div>
</div>

<section class="abs testi">
  <h2>WHAT OUR CLIENTS SAY ABOUT US</h2>
  <p>"I was worried about picking the wrong plan when I turned 65. My Elderwell agent called me the same day, compared three plans for me and explained every cost in plain words. I now pay less each month and I still see my own doctor. I recommend them to all my friends at church."</p>
  <div class="avatar" role="img" aria-label="Portrait of a happy client"></div>
  <div class="name">REED CALLOWAY</div>
  <div class="role">HAPPY CLIENT</div>
  <div class="dots"><i class="on"></i><i></i><i></i></div>
</section>

<div class="abs contact" role="img" aria-label="Dark background with a faint world map texture"></div>
<div class="abs contact-title">Contact Us</div>
<form class="abs form">
  <h4>Request a free quote</h4>
  <div class="field">Name</div>
  <div class="field">Phone or Email</div>
  <div class="field big">Message</div>
  <span class="btn">SUBMIT</span>
</form>
<div class="abs info">
  <h3>A Full Service Supplement Agency.</h3>
  <div class="offices">
    <div class="office">
      <h4>Head Office</h4>
      <p><svg width="12" height="16" viewBox="0 0 12 16" fill="#fff"><path d="M6 0a6 6 0 016 6c0 4-6 10-6 10S0 10 0 6a6 6 0 016-6z"/></svg>1801 Walnut Ave<br>Suite 300<br>Des Moines, IA 50309</p>
      <p><svg width="12" height="12" viewBox="0 0 24 24" fill="#fff"><path d="M6.6 10.8a15 15 0 006.6 6.6l2.2-2.2a1 1 0 011-.25 11.4 11.4 0 003.6.57 1 1 0 011 1V20a1 1 0 01-1 1A17 17 0 013 4a1 1 0 011-1h3.5a1 1 0 011 1c0 1.25.2 2.45.57 3.6a1 1 0 01-.25 1z"/></svg>Phone: +1 (515) 555-0148</p>
    </div>
    <div class="office">
      <h4>West Office</h4>
      <p><svg width="12" height="16" viewBox="0 0 12 16" fill="#fff"><path d="M6 0a6 6 0 016 6c0 4-6 10-6 10S0 10 0 6a6 6 0 016-6z"/></svg>2014 Harbor Pkwy<br>Suite 400<br>Urbandale, IA 50322</p>
    </div>
    <div class="office">
      <h4>Client Service Center</h4>
      <p><svg width="12" height="16" viewBox="0 0 12 16" fill="#fff"><path d="M6 0a6 6 0 016 6c0 4-6 10-6 10S0 10 0 6a6 6 0 016-6z"/></svg>284 W Grand Road<br>Suite 200<br>Clive, IA 50325</p>
      <p><svg width="12" height="12" viewBox="0 0 24 24" fill="#fff"><path d="M6.6 10.8a15 15 0 006.6 6.6l2.2-2.2a1 1 0 011-.25 11.4 11.4 0 003.6.57 1 1 0 011 1V20a1 1 0 01-1 1A17 17 0 013 4a1 1 0 011-1h3.5a1 1 0 011 1c0 1.25.2 2.45.57 3.6a1 1 0 01-.25 1z"/></svg>Phone: +1 (515) 555-0176</p>
    </div>
  </div>
</div>
<div class="abs book">FREE QUOTE</div>

<footer class="abs footer">© 2017 Go Elderwell Solutions. All Rights Reserved.</footer>

</body>
</html>
```